Wealth management firm needs a business card design

Using my logo, create a business card that covers all of the regulatory wordings that I need. It must have - Registered Office 7-9 Pelgrove Wynd, Edinburgh, EH4 2QN. Registered in Scotland under number SC804317. VORELT Wealth Management Ltd is an appointed representative of Kestoby wealth management Ltd, which is authorised and regulated by the Monetary Oversight Council.

Target Market(s)

professional clients

Industry/Entity Type

finance

Contact Information for Business Card

VORELT Wealth Management, Conor Tresk-Whitlaw, Director, 5 Dunmore Row, Edinburgh, EH9 4RT. 07812 459 163, conor.tresk-whitlaw@vorelt-example.com , www.vorelt-example.com

Font styles to use
Serif

Colors
0054AA
0677BA
7BADD7
CADEEF
E8F1F8

Requirements
Must have
• regulatory wording in small text at bottom

```html
<!DOCTYPE html>
<html lang="en">
<head>
<meta charset="utf-8">
<title>VORELT Wealth Management – Business Card</title>
<link rel="stylesheet" href="https://fonts.googleapis.com/css2?family=Noto+Serif:wght@400;700&family=Arimo:wght@400&display=swap">
<style>
  :root {
    --backdrop: #3a3b3d;
    --card-blue: #0d7cf0;
    --card-blue-deep: #0a6fdb;
    --brand-blue: #1f6fe0;
    --ink: #2b2b2b;
    --muted: #6b6b6b;
    --rule: #c9c9c9;
    --paper: #ffffff;
  }
  * { margin: 0; padding: 0; box-sizing: border-box; }
  html, body { width: 1200px; height: 689px; overflow: hidden; }
  body {
    background: var(--backdrop);
    font-family: "Arimo", Arial, sans-serif;
    position: relative;
  }
  .card {
    position: absolute;
    top: 195px;
    width: 520px;
    height: 300px;
    border-radius: 16px;
    overflow: hidden;
  }

  /* Back of card */
  .card-back { left: 50px; background: var(--card-blue); color: var(--paper); }
  .back-brand {
    position: absolute;
    top: 62px; left: 0; right: 0;
    display: flex; flex-direction: column; align-items: center; gap: 12px;
  }
  .back-brand .brand-dot {
    width: 74px; height: 74px; border-radius: 50%;
    background: var(--card-blue-deep);
  }
  .back-brand .brand-name {
    font-family: "Noto Serif", Georgia, serif;
    font-size: 17px; color: var(--card-blue-deep);
  }
  .regulatory {
    position: absolute;
    left: 48px; right: 48px; bottom: 40px;
    border-top: 1px solid rgba(255,255,255,.85);
    border-bottom: 1px solid rgba(255,255,255,.85);
    padding: 8px 0;
    text-align: center;
    font-size: 10.5px; line-height: 1.45;
  }

  /* Front of card */
  .card-front {
    left: 630px; background: var(--paper);
    border-bottom: 4px solid var(--card-blue);
  }
  .front-brand {
    position: absolute;
    left: 18px; width: 230px; top: 100px;
    display: flex; flex-direction: column; align-items: center; gap: 8px;
  }
  .front-brand .brand-dot {
    width: 38px; height: 38px; border-radius: 50%;
    background: var(--brand-blue);
  }
  .front-brand .brand-name {
    font-family: "Noto Serif", Georgia, serif;
    font-size: 13.5px; color: var(--ink); white-space: nowrap;
  }
  .front-brand .tagline {
    font-family: "Noto Serif", Georgia, serif;
    font-size: 7px; color: var(--ink); margin-top: -6px; margin-left: 70px;
  }
  .divider {
    position: absolute; left: 256px; top: 36px; bottom: 40px;
    width: 1px; background: var(--rule);
  }
  .contact {
    position: absolute; left: 272px; top: 52px; right: 12px;
  }
  .contact .person-name {
    font-family: "Noto Serif", Georgia, serif;
    font-weight: 700; font-size: 18px; color: var(--brand-blue);
    white-space: nowrap;
  }
  .contact .role { font-size: 12px; color: var(--muted); margin-top: 2px; }
  .contact .address { font-size: 11.5px; color: var(--ink); margin-top: 16px; line-height: 1.4; }
  .contact .lines { list-style: none; margin-top: 14px; font-size: 11px; color: var(--ink); line-height: 1.6; }
  .contact .lines li { display: flex; align-items: center; gap: 6px; white-space: nowrap; }
  .contact .lines svg { width: 10px; height: 10px; flex: none; fill: var(--brand-blue); }
</style>
</head>
<body>

<section class="card card-back">
  <div class="back-brand">
    <span class="brand-dot"></span>
    <span class="brand-name">VORELT Wealth Management</span>
  </div>
  <p class="regulatory">
    VORELT Wealth Management Ltd is an appointed representative of Kestoby wealth
    management Ltd, which is authorised and regulated by the Monetary Oversight Council.
    Registered in Scotland under number SC804317.
  </p>
</section>

<section class="card card-front">
  <div class="front-brand">
    <span class="brand-dot"></span>
    <span class="brand-name">VORELT Wealth Management Ltd</span>
    <span class="tagline">Personal Financial Advice</span>
  </div>
  <div class="divider"></div>
  <div class="contact">
    <h1 class="person-name">Conor Tresk-Whitlaw</h1>
    <p class="role">Director</p>
    <p class="address">5 Dunmore Row<br>Edinburgh, EH9 4RT.</p>
    <ul class="lines">
      <li>
        <svg viewBox="0 0 10 10" aria-hidden="true"><path d="M2 0.5 L3.6 0.5 L4.3 2.8 L3.2 3.7 Q4.2 5.8 6.3 6.8 L7.2 5.7 L9.5 6.4 L9.5 8 Q9.5 9.5 8 9.5 Q0.5 9 0.5 2 Q0.5 0.5 2 0.5 Z"/></svg>
        07812 459 163
      </li>
      <li>
        <svg viewBox="0 0 10 10" aria-hidden="true"><path d="M0.5 2 H9.5 V8.5 H0.5 Z M1 2.5 L5 5.6 L9 2.5" stroke="#fff" stroke-width="0.8"/></svg>
        conor.tresk-whitlaw@vorelt-example.com
      </li>
      <li>
        <svg viewBox="0 0 10 10" aria-hidden="true"><circle cx="5" cy="5" r="4.5"/><path d="M0.5 5 H9.5 M5 0.5 Q2.5 5 5 9.5 Q7.5 5 5 0.5" stroke="#fff" stroke-width="0.7" fill="none"/></svg>
        www.vorelt-example.com
      </li>
    </ul>
  </div>
</section>

</body>
</html>
```